Falcrest security business card

Looking for a business card for my security company

Target Market(s)

Security

Industry/Entity Type

Security

Contact Information for Business Card

Name - Gil Marston. Title - General manager - direct 314 862.4490 website www. falcrestsecurityservices.example email - gil@ falcrestsecurityservices.example

Requirements
Must have
• Logo attached

```html
<!DOCTYPE html>
<html lang="en">
<head>
<meta charset="utf-8">
<title>Falcrest Security Services – Business Card</title>
<link href="https://fonts.googleapis.com/css2?family=Montserrat:wght@700&family=Roboto:wght@400&display=swap" rel="stylesheet">
<style>
  :root {
    --page-bg: #2a2a2c;
    --card-bg: #141414;
    --card-edge: #1c1c1c;
    --gold: #c9a24a;
    --gold-light: #e2c173;
    --pattern-dark: #161616;
    --pattern-mid: #2c2c2c;
  }
  * { margin: 0; padding: 0; box-sizing: border-box; }
  html, body {
    width: 1200px;
    height: 900px;
    overflow: hidden;
    background: var(--page-bg);
  }
  .sheet {
    width: 1200px;
    height: 900px;
    display: flex;
    flex-direction: column;
    align-items: center;
    justify-content: center;
    gap: 40px;
  }
  .card {
    width: 700px;
    height: 400px;
    border-radius: 22px;
    background: var(--card-bg);
    border: 1px solid var(--card-edge);
    box-shadow: 0 10px 30px rgba(0,0,0,0.45);
    position: relative;
    overflow: hidden;
  }
  .card--front {
    display: flex;
    align-items: center;
  }
  .brand {
    width: 330px;
    display: flex;
    justify-content: center;
    align-items: center;
  }
  .brand__name {
    font-family: "Montserrat", sans-serif;
    font-weight: 700;
    font-size: 46px;
    letter-spacing: 1px;
    text-transform: uppercase;
    color: var(--gold);
  }
  .divider {
    width: 1px;
    height: 150px;
    background: var(--gold);
  }
  .contact {
    padding-left: 34px;
    color: var(--gold);
  }
  .contact__name {
    font-family: "Montserrat", sans-serif;
    font-weight: 700;
    font-size: 34px;
    line-height: 1;
    text-transform: uppercase;
    color: var(--gold-light);
  }
  .contact__title {
    font-family: "Roboto", sans-serif;
    font-size: 17px;
    margin: 6px 0 14px;
  }
  .contact__list { list-style: none; }
  .contact__item {
    font-family: "Roboto", sans-serif;
    font-size: 16px;
    line-height: 26px;
    display: flex;
    align-items: center;
    gap: 8px;
  }
  .contact__icon {
    width: 13px;
    height: 13px;
    flex: none;
  }
  .card--back .pattern {
    position: absolute;
    inset: 0;
    background: linear-gradient(135deg, var(--pattern-dark) 0%, var(--pattern-mid) 45%, var(--pattern-dark) 100%);
  }
</style>
</head>
<body>
  <main class="sheet">
    <section class="card card--front">
      <div class="brand">
        <span class="brand__name">Falcrest</span>
      </div>
      <div class="divider"></div>
      <div class="contact">
        <h1 class="contact__name">Gil Marston</h1>
        <p class="contact__title">General manager</p>
        <ul class="contact__list">
          <li class="contact__item">
            <svg class="contact__icon" viewBox="0 0 24 24" fill="none" stroke="var(--gold)" stroke-width="2.2" stroke-linecap="round" stroke-linejoin="round"><path d="M5 3h4l2 5-3 2a11 11 0 0 0 6 6l2-3 5 2v4a2 2 0 0 1-2 2A17 17 0 0 1 3 5a2 2 0 0 1 2-2z"/></svg>
            314 862.4490
          </li>
          <li class="contact__item">
            <svg class="contact__icon" viewBox="0 0 24 24" fill="none" stroke="var(--gold)" stroke-width="2.2" stroke-linejoin="round"><rect x="2" y="5" width="20" height="14" rx="1"/><path d="M2 6l10 7 10-7"/></svg>
            gil@ falcrestsecurityservices.example
          </li>
          <li class="contact__item">
            <svg class="contact__icon" viewBox="0 0 24 24" fill="none" stroke="var(--gold)" stroke-width="2"><circle cx="12" cy="12" r="10"/><path d="M2 12h20M12 2c3 3 3 17 0 20M12 2c-3 3-3 17 0 20"/></svg>
            www. falcrestsecurityservices.example
          </li>
        </ul>
      </div>
    </section>

    <section class="card card--back">
      <div class="pattern" role="img" aria-label="Repeating pattern of leaping big cat silhouettes in dark grey tones"></div>
    </section>
  </main>
</body>
</html>
```